Harbinger Slabworks, Inc. Business Card

Create a business card that is eye catching and based around concrete sawcutting. I've attached our current business card and logo for reference. We like aspects of the current business card, but it is starting to feel very loud and lost. We would like something that is still fun but is more modern and streamlined.

```html
<!DOCTYPE html>
<html lang="en">
<head>
<meta charset="utf-8">
<title>Harbinger Slabworks, Inc. Business Card</title>
<link rel="stylesheet" href="https://fonts.googleapis.com/css2?family=Montserrat:wght@500;700;800&display=swap">
<style>
  :root {
    --page: #3a3c40;
    --card-top: #1c1c1e;
    --card-bottom: #0b0b0c;
    --silver-light: #f2f2f2;
    --silver-mid: #b9b9bb;
    --silver-dark: #6d6d70;
    --text-light: #e6e6e6;
    --text-dark: #141414;
    --mark-ring: #c7c8ca;
  }
  * { box-sizing: border-box; margin: 0; padding: 0; }
  html, body { width: 1200px; height: 952px; overflow: hidden; }
  body {
    background: var(--page);
    font-family: "Montserrat", sans-serif;
    display: flex;
    align-items: center;
    justify-content: center;
    gap: 40px;
  }
  .card {
    position: relative;
    width: 540px;
    height: 309px;
    border-radius: 18px;
    overflow: hidden;
    background: linear-gradient(160deg, var(--card-top), var(--card-bottom));
    box-shadow: 0 14px 30px rgba(0,0,0,.45);
  }
  .brand {
    position: absolute;
    display: flex;
    align-items: center;
    gap: 12px;
  }
  .brand-dot {
    width: 46px; height: 46px;
    border-radius: 50%;
    border: 4px solid var(--mark-ring);
    flex: none;
  }
  .brand-name {
    font-weight: 800;
    font-size: 17px;
    line-height: 1.15;
    letter-spacing: .08em;
    color: var(--text-light);
    text-transform: uppercase;
  }
  /* front */
  .front .brand { left: 34px; top: 46px; }
  .front .chrome-edge {
    position: absolute; left: 0; bottom: 0; width: 100%; height: 10px;
    background: linear-gradient(90deg, var(--silver-dark), var(--silver-light) 45%, var(--silver-mid));
    clip-path: polygon(0 0, 38% 0, 41% 100%, 0 100%);
  }
  .front .chrome-edge-right {
    position: absolute; right: 0; bottom: 0; width: 59%; height: 10px;
    background: linear-gradient(90deg, var(--silver-mid), var(--silver-light));
  }
  .contact {
    position: absolute; left: 246px; top: 48px; right: 24px;
    color: var(--text-light);
  }
  .person-name {
    font-weight: 800;
    font-size: 25px;
    letter-spacing: .03em;
    text-transform: uppercase;
    background: linear-gradient(180deg, #ffffff, #a9a9ab);
    -webkit-background-clip: text; background-clip: text; color: transparent;
    margin-bottom: 16px;
  }
  .phones { display: flex; align-items: center; gap: 10px; margin-bottom: 10px; }
  .phone-icon {
    width: 28px; height: 28px; border-radius: 5px;
    background: linear-gradient(135deg, var(--silver-light), var(--silver-dark));
    display: flex; align-items: center; justify-content: center; flex: none;
  }
  .phone-list { font-size: 13px; font-weight: 500; line-height: 1.3; }
  .email, .address { font-size: 13px; font-weight: 500; line-height: 1.45; }
  .email { margin-bottom: 6px; }
  /* back */
  .back .brand { left: 150px; top: 52px; }
  .services {
    position: absolute; right: 0; bottom: 38px;
    list-style: none;
    display: flex; flex-direction: column; gap: 9px; align-items: flex-end;
  }
  .service {
    height: 26px;
    padding: 0 24px 0 34px;
    display: flex; align-items: center;
    font-weight: 800; font-size: 12px; letter-spacing: .06em;
    color: var(--text-dark);
    text-transform: uppercase;
    background: linear-gradient(90deg, var(--silver-dark), var(--silver-light) 30%, var(--silver-mid));
    clip-path: polygon(22px 0, 100% 0, 100% 100%, 0 100%);
  }
  .service:nth-child(1) { width: 190px; }
  .service:nth-child(2) { width: 230px; }
  .service:nth-child(3) { width: 270px; }
  .service:nth-child(4) { width: 310px; }
</style>
</head>
<body>
  <section class="card front" aria-label="Card front">
    <div class="brand">
      <span class="brand-dot"></span>
      <span class="brand-name">Harbinger<br>Slabworks</span>
    </div>
    <div class="contact">
      <h1 class="person-name">Marisa Delvecchio</h1>
      <div class="phones">
        <span class="phone-icon">
          <svg width="16" height="16" viewBox="0 0 24 24" aria-hidden="true">
            <path fill="#1a1a1a" d="M6.6 10.8a15.1 15.1 0 0 0 6.6 6.6l2.2-2.2a1 1 0 0 1 1-.25 11.4 11.4 0 0 0 3.6.57 1 1 0 0 1 1 1V20a1 1 0 0 1-1 1A17 17 0 0 1 3 4a1 1 0 0 1 1-1h3.5a1 1 0 0 1 1 1c0 1.25.2 2.45.57 3.57a1 1 0 0 1-.25 1z"/>
          </svg>
        </span>
        <div class="phone-list">
          <div>555.010.4821</div>
          <div>555.010.7733</div>
        </div>
      </div>
      <div class="email">Marisa@HarbingerSlabworks.com</div>
      <div class="address">48 Quarry Lane<br>Millbrook, NJ 07000</div>
    </div>
    <div class="chrome-edge"></div>
    <div class="chrome-edge-right"></div>
  </section>

  <section class="card back" aria-label="Card back">
    <div class="brand">
      <span class="brand-dot"></span>
      <span class="brand-name">Harbinger<br>Slabworks</span>
    </div>
    <ul class="services">
      <li class="service">Core Drilling</li>
      <li class="service">Wall Sawing</li>
      <li class="service">Slab Sawing</li>
      <li class="service">Breaking &amp; Removal</li>
    </ul>
  </section>
</body>
</html>
```